New Wordpress, web design and a logo for a text analysis website. The website name is Quorvela.com

Task Description- We are looking for an exciting design for a new textual analysis website in Wordpress. The website enables individuals (initially only academics, but this might be expanded later) to upload textual data (e.g. excel files) for processing and download textual analysis results. For example, users can upload data with hundreds of Excel cells containing text and receive back analysis of the positive/negative sentiment in that text, the count of complex words, the count of numbers, the most frequent terms, or similarity of text in the uploaded database. The landing page will explain the concept and vision of the website, will perhaps visually illustrate the ease with which it can be done (files uploaded and results downloaded with no need for technical knowledge). Hence, we want to communicate that we provide an easy to use, yet powerful tool. Although we do not have images to share, we would like the website to include images and graphic images, you may use stock images in your design.

Logo- The design should include a logo with the word “Quorvela” and perhaps a magnifying glass enlarging text, but we are open to some creative thinking of the logo. Overall, we are hoping to communicate the following terms: “textual analysis” and “analytics”.
Pages- The design should include at least the following pages (each should include a logo, header, body, background, navigation menu and a footer)

1. Home page, describing the overall objective to enable easy analysis of textual data. The background/images should likely illustrate text going into a magnifying glass/a computer/ or another automation-related and graphs (pie chart, bar chart, etc.), or other outputs, are coming out of the other side. We are open to all other creative suggestions to illustrate this process.
2. Tools- this page will list the different textual analysis tools that the website is offering and briefly explain each. Each of these tools is a link to its own page where the tool can be applied. Examples of tools that will be included are (1) Count of words and numbers (2) sentiment analysis (3) custom uploaded dictionary of words analysis (4) Similarity analysis (5) N-gram analysis of frequent single or multiple words.
3. Design of one tool page (we will replicate the design ourselves for other tools)- Each page will include an explanation of the procedure and files the users should prepare. Each page should also include forms that allow the users to (1) Browse their computer to upload their text file (2) drop down select boxes (3) radio buttons or check boxes. We will change the number of these boxes ourselves in the future.
4. Registration/Login- a standard registration page, asking users for name (first and last), email, set a password and confirm it. And also, allowing existing users to login.
5. About page- a page that includes information about the two researchers, including a photo and a short text describing their background.
6. News- a page describing news and media mentions of the page and links to research papers that used the tool.
Colors- The project is developed by researchers from two universities and the colors of both schools should be incorporated into the design. The primary colors of red and blue should be prominent. The color codes are in the following links (1) https://brand.halvermoor.edu/guide/design-elements/colors/ (2) https://www.ostrander.edu/offices/marketing-communications/ostrander-brand/brand-assets/ostrander-color-palette

Quorvela

```html
<!DOCTYPE html>
<html lang="en">
<head>
<meta charset="utf-8">
<title>Quorvela – Textual Analysis</title>
<link href="https://fonts.googleapis.com/css2?family=Roboto:wght@400;500;700&display=swap" rel="stylesheet">
<style>
  :root {
    --brand-blue: #0080c6;
    --brand-blue-deep: #0a73b5;
    --brand-red: #e8336b;
    --ink: #111111;
    --body-text: #3a3a3a;
    --white: #ffffff;
    --footer-bg: #060606;
    --footer-text: #e9e9e9;
    --divider: #2a2a2a;
  }
  * { box-sizing: border-box; margin: 0; padding: 0; }
  html, body { width: 829px; height: 1200px; overflow: hidden; }
  body {
    position: relative;
    font-family: "Roboto", Arial, sans-serif;
    background: var(--white);
    color: var(--ink);
  }
  .abs { position: absolute; }

  /* Hero */
  .hero-bg { left: 0; top: 0; width: 829px; height: 480px; }
  .brand { left: 77px; top: 28px; display: flex; align-items: center; gap: 6px;
    color: var(--white); font-weight: 700; font-size: 22px; letter-spacing: -0.2px; }
  .brand-dot { width: 12px; height: 12px; border: 2px solid var(--white); border-radius: 50%; }
  .main-nav { top: 40px; left: 0; width: 829px; height: 14px; }
  .main-nav a { position: absolute; color: var(--white); text-decoration: none;
    font-weight: 500; font-size: 10.5px; }
  .btn-register { left: 691px; top: 31px; width: 88px; height: 34px;
    border: 1.5px solid var(--white); border-radius: 4px; color: var(--white);
    font-weight: 500; font-size: 9.5px; display: flex; align-items: center; justify-content: center; }
  .hero-title { left: 45px; top: 136px; width: 390px; color: var(--white);
    font-weight: 700; font-size: 24px; line-height: 38px; text-transform: uppercase; }
  .hero-sub { left: 48px; top: 255px; width: 300px; color: var(--white);
    font-weight: 700; font-size: 9.6px; line-height: 16.5px; text-transform: uppercase; }
  .btn-outline-light { left: 47px; top: 304px; width: 116px; height: 40px;
    border: 1.5px solid var(--white); border-radius: 20px; color: var(--white);
    font-weight: 500; font-size: 11px; display: flex; align-items: center; justify-content: center; }
  .hero-art { left: 346px; top: 100px; width: 441px; height: 309px; border-radius: 24px;
    background: linear-gradient(135deg, rgba(255,255,255,0.28), rgba(120,150,240,0.35) 55%, rgba(232,51,107,0.35)); }

  /* Tool cards */
  .tool-card { background: var(--white); width: 157px; height: 187px;
    box-shadow: 0 2px 8px rgba(0,0,0,0.12); text-align: center; }
  .tool-art { position: absolute; border-radius: 6px; }
  .tool-title { position: absolute; left: 0; width: 100%; font-weight: 500;
    font-size: 12.5px; line-height: 16.5px; color: var(--ink); }
  .tool-text { position: absolute; left: 0; width: 100%; font-size: 10.2px;
    line-height: 16.5px; color: var(--body-text); }

  /* About */
  .about-title { left: 450px; top: 550px; color: var(--brand-blue-deep);
    font-weight: 700; font-size: 24px; }
  .about-text { left: 450px; top: 602px; width: 300px; font-size: 10.5px;
    line-height: 16.6px; color: var(--body-text); }
  .btn-outline-blue { left: 449px; top: 706px; width: 105px; height: 41px;
    border: 1.5px solid var(--brand-blue-deep); border-radius: 21px; color: var(--brand-blue-deep);
    font-weight: 500; font-size: 10.5px; display: flex; align-items: center; justify-content: center; }

  /* Footer */
  .site-footer { left: 0; top: 905px; width: 829px; height: 295px; background: var(--footer-bg); color: var(--footer-text); }
  .footer-brand { left: 77px; top: 58px; display: flex; align-items: center; gap: 6px;
    color: var(--white); font-weight: 700; font-size: 22px; }
  .footer-about { left: 77px; top: 90px; width: 175px; font-size: 10.5px; line-height: 16.6px; }
  .footer-heading { top: 59px; color: var(--white); font-weight: 700; font-size: 12.5px; }
  .quick-links { left: 310px; top: 86px; list-style: none; font-size: 10.5px; line-height: 22px; }
  .contact-list { left: 444px; top: 90px; font-size: 10.5px; line-height: 16.6px; }
  .contact-item { position: absolute; left: 24px; white-space: nowrap; }
  .social { top: 88px; width: 24px; height: 24px; border-radius: 50%; background: var(--brand-blue); }
  .footer-rule { left: 77px; top: 205px; width: 675px; height: 1px; background: var(--divider); }
  .copyright { left: 0; top: 238px; width: 829px; text-align: center; font-size: 10.5px; }
</style>
</head>
<body>

<header>
  <svg class="abs hero-bg" viewBox="0 0 829 480" aria-hidden="true">
    <path d="M0 0 H829 V432 C790 450 740 478 680 474 C600 468 520 385 414 388 C300 392 220 470 120 472 C70 472 30 452 0 435 Z" fill="var(--brand-blue)"/>
  </svg>

  <div class="abs brand"><span class="brand-dot"></span>Quorvela</div>

  <nav class="abs main-nav">
    <a style="left:396px">HOME</a>
    <a style="left:450px">TOOLS</a>
    <a style="left:510px">ABOUT</a>
    <a style="left:571px">NEWS</a>
    <a style="left:627px">CONTACT</a>
  </nav>
  <div class="abs btn-register">REGISTRATION</div>

  <h1 class="abs hero-title">Analytics is the systematic computational analysis of data or statistics.</h1>
  <p class="abs hero-sub">Sed ut perspiciatis unde omnis iste natus error sit voluptatem accusantium</p>
  <div class="abs btn-outline-light">LEARN MORE</div>

  <div class="abs hero-art" role="img" aria-label="Isometric illustration of two analysts with a magnifying glass, bar charts, pie chart and data panels"></div>
</header>

<main>
  <section class="abs tool-card" style="left:77px;top:447px">
    <div class="tool-art" style="left:33px;top:15px;width:82px;height:71px;background:linear-gradient(135deg,#e3e8fb,#c9d3f5)" role="img" aria-label="Small isometric illustration of people counting words and numbers"></div>
    <h3 class="tool-title" style="top:95px">Count of words<br>and numbers</h3>
    <p class="tool-text" style="top:136px">Sed ut perspiciatis unde<br>omnis iste natus error</p>
  </section>

  <section class="abs tool-card" style="left:253px;top:549px">
    <div class="tool-art" style="left:31px;top:19px;width:98px;height:74px;background:linear-gradient(135deg,#dfe6fb,#f6d3e3)" role="img" aria-label="Small isometric illustration of a team comparing documents"></div>
    <h3 class="tool-title" style="top:107px">Similarity analysis</h3>
    <p class="tool-text" style="top:135px">Sed ut perspiciatis unde<br>omnis iste natus error</p>
  </section>

  <section class="abs tool-card" style="left:77px;top:660px">
    <div class="tool-art" style="left:18px;top:12px;width:120px;height:91px;border-radius:0;background:linear-gradient(135deg,#eef1fb,#c7d4f3)" role="img" aria-label="Small isometric illustration of people working on a large screen"></div>
    <h3 class="tool-title" style="top:117px">sentiment analysis</h3>
    <p class="tool-text" style="top:143px">Sed ut perspiciatis unde<br>omnis iste natus error</p>
  </section>

  <section>
    <h2 class="abs about-title">ABOUT</h2>
    <p class="abs about-text">Sed ut perspiciatis unde omnis iste natus error sit voluptatem accusantium doloremque laudantium, totam rem aperiam, eaque ipsa quae ab illo inventore veritatis et quasi architecto beatae vitae dicta sunt explicabo. Nemo enim ipsam voluptatem quia voluptas sit aspernatur aut odit aut fugit</p>
    <div class="abs btn-outline-blue">LEARN MORE</div>
  </section>
</main>

<footer class="abs site-footer">
  <div class="abs footer-brand"><span class="brand-dot"></span>Quorvela</div>
  <p class="abs footer-about">Nemo enim ipsam voluptatem quia voluptas sit aspernatur aut odit aut fugit, sed quia consequuntur magni dolores eos qui ratione voluptatem sequi nesciunt.</p>

  <h4 class="abs footer-heading" style="left:308px">QUICK LINK</h4>
  <ul class="abs quick-links">
    <li>HOME</li><li>ABOUT</li><li>TOOLS</li><li>NEWS</li><li>CONTACT</li>
  </ul>

  <h4 class="abs footer-heading" style="left:444px">CONTACT US</h4>
  <div class="abs contact-list">
    <svg class="abs" style="left:3px;top:2px" width="14" height="18" viewBox="0 0 14 18" aria-hidden="true">
      <path d="M7 0C3.1 0 0 3 0 6.8 0 11.6 7 18 7 18s7-6.4 7-11.2C14 3 10.9 0 7 0z" fill="var(--brand-blue)"/>
      <circle cx="7" cy="6.6" r="2.6" fill="var(--footer-bg)"/>
    </svg>
    <span class="contact-item" style="top:0">105 sreet name city name<br>country name</span>
    <svg class="abs" style="left:4px;top:40px" width="11" height="18" viewBox="0 0 11 18" aria-hidden="true">
      <rect x="1" y="1" width="9" height="16" rx="2" fill="none" stroke="var(--brand-blue)" stroke-width="1.6"/>
      <circle cx="5.5" cy="14" r="0.9" fill="var(--brand-blue)"/>
    </svg>
    <span class="contact-item" style="top:41px">999-999-9999</span>
    <svg class="abs" style="left:1px;top:70px" width="16" height="11" viewBox="0 0 16 11" aria-hidden="true">
      <rect width="16" height="11" fill="var(--brand-blue)"/>
      <path d="M0 0 L8 6 L16 0" fill="none" stroke="var(--footer-bg)" stroke-width="1.2"/>
    </svg>
    <span class="contact-item" style="top:66px">hello@quorvela.com</span>
  </div>

  <h4 class="abs footer-heading" style="left:668px">FOLLOW US</h4>
  <div class="abs social" style="left:667px" role="img" aria-label="Social profile link"></div>
  <div class="abs social" style="left:697px" role="img" aria-label="Video channel link"></div>
  <div class="abs social" style="left:726px" role="img" aria-label="Photo profile link"></div>

  <div class="abs footer-rule"></div>
  <p class="abs copyright">© Quorvela All Rights Reserved</p>
</footer>

</body>
</html>
```